Wow me with your Earring card options!

An A7 portrait sized earring card is required for Velvet & Vinyl. Inspired by Velvet and fueled by Vinyl we love our accessories to do the talking. Bold statement earrings are our thing. Our earring cards need to showcase our brand while not stealing all of the limelight from the earrings themselves. Earring care information needs to be included on the back side of the card. Our simple logo needs to be the basis for the colour choices used on the card.

Need extra days to review

• No florals please 😊

```html
<!DOCTYPE html>
<html lang="en">
<head>
<meta charset="utf-8">
<title>Velvet &amp; Vinyl — Earring Card</title>
<link rel="stylesheet" href="https://fonts.googleapis.com/css2?family=Montserrat:wght@500;800&family=Kaushan+Script&display=swap">
<style>
  :root {
    --page: #f1f0ee;
    --card-dark: #000000;
    --card-light: #ffffff;
    --ink: #2a2a2a;
    --grey-script: #6e6e6e;
    --teal: #0f6e6e;
    --teal-soft: #bfe3df;
    --violet: #5b1fd6;
    --violet-soft: #dccdf9;
    --pink: #e0218a;
    --pink-soft: #f8c8e2;
    --orange: #f0641e;
    --orange-soft: #fcd6bd;
    --l-teal: #0f7a7a;
    --l-green: #2bb04a;
    --l-yellow: #f2c11d;
    --l-orange: #f27a1a;
    --l-pink: #e0218a;
    --l-violet: #6a1fe0;
    --l-black: #151515;
    --wash-dark-green: #24401f;
    --wash-rust: #8a3a14;
    --wash-plum: #7a1850;
    --wash-indigo: #4a1fa8;
    --wash-deep-teal: #0a7373;
    --wash-mint: #a6dca0;
    --wash-peach: #f7b48f;
    --wash-rose: #f6bcd9;
    --wash-lilac: #cbb8ef;
    --wash-aqua: #9fd8d6;
  }
  * { box-sizing: border-box; margin: 0; padding: 0; }
  html, body { width: 1186px; height: 1200px; overflow: hidden; }
  body {
    background: var(--page);
    font-family: "Montserrat", Arial, sans-serif;
    position: relative;
  }
  .card {
    position: absolute;
    top: 232px;
    width: 520px;
    height: 735px;
    overflow: hidden;
  }
  .card--front { left: 50px; background: var(--card-dark); }
  .card--back  { left: 616px; background: var(--card-light); }

  .wash { position: absolute; left: 0; width: 520px; }
  .front-wash-top {
    top: 0; height: 190px;
    background: linear-gradient(100deg, var(--wash-dark-green), var(--wash-rust));
    opacity: .55;
    -webkit-mask-image: linear-gradient(to bottom, #000 30%, transparent);
            mask-image: linear-gradient(to bottom, #000 30%, transparent);
  }
  .front-wash-bottom {
    top: 380px; height: 355px;
    background: linear-gradient(115deg, var(--wash-plum), var(--wash-indigo) 55%, var(--wash-deep-teal));
    -webkit-mask-image: linear-gradient(to top, #000 55%, transparent);
            mask-image: linear-gradient(to top, #000 55%, transparent);
  }
  .back-wash-top {
    top: 0; height: 210px;
    background: linear-gradient(100deg, var(--wash-mint), var(--wash-peach));
    opacity: .6;
    -webkit-mask-image: linear-gradient(to bottom, #000 20%, transparent);
            mask-image: linear-gradient(to bottom, #000 20%, transparent);
  }
  .back-wash-bottom {
    top: 420px; height: 315px;
    background: linear-gradient(115deg, var(--wash-rose), var(--wash-lilac) 50%, var(--wash-aqua));
    opacity: .75;
    -webkit-mask-image: linear-gradient(to top, #000 50%, transparent);
            mask-image: linear-gradient(to top, #000 50%, transparent);
  }

  .front-brand {
    position: absolute;
    left: 0; right: 0; top: 92px;
    text-align: center;
    color: #ffffff;
    font-weight: 800;
    font-size: 38px;
    letter-spacing: 1px;
  }

  .back-title {
    position: absolute;
    left: 128px; top: 80px;
    font-weight: 800;
    font-size: 58px;
    letter-spacing: 1px;
    line-height: 1;
  }
  .back-title span:nth-child(1) { color: var(--l-teal); }
  .back-title span:nth-child(2) { color: var(--l-green); }
  .back-title span:nth-child(3) { color: var(--l-yellow); }
  .back-title span:nth-child(4) { color: var(--l-orange); }
  .back-title span:nth-child(5) { color: var(--l-pink); }
  .back-title span:nth-child(6) { color: var(--l-violet); }
  .back-title span:nth-child(7) { color: var(--l-black); }
  .back-subtitle {
    position: absolute;
    left: 190px; top: 128px;
    font-family: "Kaushan Script", cursive;
    font-size: 42px;
    color: var(--grey-script);
    transform: rotate(-6deg);
    transform-origin: left bottom;
  }

  .care-list { list-style: none; }
  .care-item {
    position: absolute;
    left: 50px;
    width: 420px;
    height: 44px;
  }
  .care-item .pill {
    position: absolute;
    left: 40px; right: 0; top: 2px;
    height: 40px;
    border: 2px solid;
    border-radius: 20px;
    display: flex;
    align-items: center;
    padding-left: 30px;
    font-size: 14.5px;
    font-weight: 500;
  }
  .care-item svg { position: absolute; left: 0; top: -8px; width: 60px; height: 60px; }
  .care-item--water { top: 272px; color: var(--teal); }
  .care-item--water .pill { background: var(--teal-soft); border-color: var(--teal); }
  .care-item--bed { top: 343px; color: var(--violet); }
  .care-item--bed .pill { background: var(--violet-soft); border-color: var(--violet); }
  .care-item--perfume { top: 419px; color: var(--pink); }
  .care-item--perfume .pill { background: var(--pink-soft); border-color: var(--pink); }
  .care-item--sun { top: 493px; color: var(--orange); }
  .care-item--sun .pill { background: var(--orange-soft); border-color: var(--orange); }

  .contact {
    position: absolute;
    font-size: 11.5px;
    color: var(--ink);
    display: flex;
    align-items: center;
    gap: 10px;
  }
  .contact svg { width: 14px; height: 14px; }
  .contact--web { left: 18px; top: 616px; }
  .contact--mail { left: 18px; top: 639px; }
  .contact--social { left: 362px; top: 639px; }

  .back-logo {
    position: absolute;
    left: 259px; top: 589px;
    width: 86px; height: 86px;
    border-radius: 50%;
    background: var(--card-dark);
    color: #ffffff;
    font-weight: 800;
    font-size: 12px;
    display: flex;
    align-items: center;
    justify-content: center;
    text-align: center;
    line-height: 1.2;
  }
</style>
</head>
<body>

<section class="card card--front">
  <div class="wash front-wash-top" role="img" aria-label="Dark green and rust watercolour coffee-ring splashes"></div>
  <div class="wash front-wash-bottom" role="img" aria-label="Magenta, violet, teal and yellow watercolour paint splashes"></div>
  <h1 class="front-brand">VELVET &amp; VINYL</h1>
</section>

<section class="card card--back">
  <div class="wash back-wash-top" role="img" aria-label="Soft green and peach watercolour coffee-ring splashes"></div>
  <div class="wash back-wash-bottom" role="img" aria-label="Pastel pink, lilac, aqua and yellow watercolour splashes"></div>

  <h2 class="back-title"><span>E</span><span>A</span><span>R</span><span>R</span><span>I</span><span>N</span><span>G</span></h2>
  <p class="back-subtitle">Care instruction</p>

  <ul class="care-list">
    <li class="care-item care-item--water">
      <span class="pill">Avoid moisture and remove before bathing</span>
      <svg viewBox="0 0 60 60" aria-hidden="true">
        <path d="M24 6 C24 6 8 28 8 38 a16 16 0 0 0 32 0 C40 28 24 6 24 6Z" fill="currentColor"/>
        <path d="M44 4 C44 4 37 14 37 18 a7 7 0 0 0 14 0 C51 14 44 4 44 4Z" fill="currentColor"/>
        <circle cx="24" cy="38" r="6" fill="none" stroke="#fff" stroke-width="3"/>
      </svg>
    </li>
    <li class="care-item care-item--bed">
      <span class="pill">For comforts sake, remove before bed</span>
      <svg viewBox="0 0 60 60" aria-hidden="true">
        <rect x="4" y="12" width="52" height="18" rx="3" fill="currentColor"/>
        <rect x="10" y="17" width="17" height="10" rx="3" fill="#fff"/>
        <rect x="33" y="17" width="17" height="10" rx="3" fill="#fff"/>
        <rect x="2" y="30" width="56" height="16" rx="2" fill="currentColor"/>
        <rect x="4" y="46" width="6" height="6" fill="currentColor"/>
        <rect x="50" y="46" width="6" height="6" fill="currentColor"/>
      </svg>
    </li>
    <li class="care-item care-item--perfume">
      <span class="pill">Avoid contact with perfumes and lotions</span>
      <svg viewBox="0 0 60 60" aria-hidden="true">
        <rect x="24" y="6" width="12" height="8" rx="1" fill="none" stroke="currentColor" stroke-width="2"/>
        <rect x="26" y="14" width="8" height="6" fill="currentColor"/>
        <rect x="12" y="20" width="36" height="36" rx="10" fill="currentColor"/>
        <circle cx="30" cy="38" r="6" fill="#fff"/>
      </svg>
    </li>
    <li class="care-item care-item--sun">
      <span class="pill">Store away from direct sunlight</span>
      <svg viewBox="0 0 60 60" aria-hidden="true">
        <circle cx="30" cy="30" r="12" fill="currentColor"/>
        <g stroke="currentColor" stroke-width="3" stroke-linecap="round">
          <line x1="30" y1="3" x2="30" y2="12"/><line x1="30" y1="48" x2="30" y2="57"/>
          <line x1="3" y1="30" x2="12" y2="30"/><line x1="48" y1="30" x2="57" y2="30"/>
          <line x1="11" y1="11" x2="17" y2="17"/><line x1="43" y1="43" x2="49" y2="49"/>
          <line x1="49" y1="11" x2="43" y2="17"/><line x1="11" y1="49" x2="17" y2="43"/>
        </g>
      </svg>
    </li>
  </ul>

  <p class="contact contact--web">
    <svg viewBox="0 0 14 14" aria-hidden="true"><circle cx="7" cy="7" r="6" fill="none" stroke="#222" stroke-width="1.2"/><ellipse cx="7" cy="7" rx="2.6" ry="6" fill="none" stroke="#222" stroke-width="1.2"/><line x1="1" y1="7" x2="13" y2="7" stroke="#222" stroke-width="1.2"/></svg>
    www.velvetandvinyl-studio.com
  </p>
  <p class="contact contact--mail">
    <svg viewBox="0 0 14 14" aria-hidden="true"><rect x="1" y="3" width="12" height="9" fill="#222"/><path d="M1 3 L7 8 L13 3" fill="none" stroke="#fff" stroke-width="1.2"/></svg>
    hello@velvetandvinyl-studio.com
  </p>
  <div class="back-logo">Velvet &amp;<br>Vinyl</div>
  <p class="contact contact--social">
    <svg viewBox="0 0 14 14" aria-hidden="true"><circle cx="7" cy="4.5" r="3" fill="#222"/><path d="M1.5 13 a5.5 5 0 0 1 11 0Z" fill="#222"/></svg>
    @velvetandvinylstudio
  </p>
</section>

</body>
</html>
```